Web Design Project

Please take a look at my current aged website www.marlowpeoplesupport.example and my newly designed logo and business cards. I would like a new fresh updated look to my website and my new designs incorporated.
Updates

  Good Morning Everyone

Due to an Austrralian licencing issue I have had to have my logo slightly redesigned.

Would you please be able to look at the newly uploaded files and revise your designs.

Thanks so much.  I am very happy with the calibre and quality of the designs so far.

kind Regards

Tessa

Industry/Entity Type

Business

Requirements
Must have
• the exisiting pages and fresh new graphics and a real commitment to my palette of lime green, turqouise and black.

```html
<!DOCTYPE html>
<html lang="en">
<head>
<meta charset="utf-8">
<title>Marlow People Support – Contact Us</title>
<link rel="stylesheet" href="https://fonts.googleapis.com/css2?family=Arimo:wght@400&family=Roboto+Condensed:wght@400&family=Source+Sans+3:ital,wght@0,400;0,600;1,700&display=swap">
<style>
:root{
  --backdrop:#9b9b9b;
  --paper:#ffffff;
  --lime:#6db33f;
  --lime-soft:#a9d18e;
  --turquoise:#2aa7c9;
  --sage:#d9e0d3;
  --ink:#000000;
  --nav-grey:#5a5a5a;
  --label-grey:#6b6b6b;
  --field-border:#6f6f6f;
}
*{box-sizing:border-box;margin:0;padding:0}
html,body{width:1082px;height:1200px;overflow:hidden;background:var(--backdrop)}
.stage{position:absolute;left:0;top:0;width:1012px;height:1122px;transform:scale(1.0692);transform-origin:0 0;font-family:"Source Sans 3",sans-serif;color:var(--ink)}
.page{position:absolute;left:175px;top:10px;width:660px;height:1066px;background:var(--paper);box-shadow:6px 6px 10px rgba(0,0,0,.55),-3px 2px 8px rgba(0,0,0,.35)}
.page-edge{position:absolute;left:0;top:0;width:21px;height:100%;background:linear-gradient(#e4e8e1 0%,#cfe0c2 45%,var(--lime) 100%)}
.header-swoosh{position:absolute;left:21px;top:0}
.brand-mark{position:absolute;left:45px;top:35px;width:95px;height:95px;border:6px solid var(--turquoise);border-radius:50%}
.brand-name{position:absolute;left:166px;top:18px;font-family:"Arimo",sans-serif;font-size:31px;color:var(--ink);white-space:nowrap}
.brand-tagline{position:absolute;left:224px;top:56px;font-family:"Arimo",sans-serif;font-size:12.5px;color:#707070;white-space:nowrap}
.main-nav a{position:absolute;font-family:"Roboto Condensed",sans-serif;font-size:17px;color:var(--nav-grey);text-decoration:none;white-space:nowrap;text-align:right}
.main-nav .current{color:var(--ink)}
.contact-tab{position:absolute;left:751px;top:305px;width:96px;height:38px;background:linear-gradient(90deg,#e7ece3,#d3ddcb);border-radius:0 0 4px 4px;box-shadow:1px 1px 3px rgba(0,0,0,.25);font-family:"Roboto Condensed",sans-serif;font-size:17px;color:#555;padding:11px 0 0 0;text-align:center}
.nav-dial{position:absolute;left:710px;top:140px}
.band{position:absolute;left:196px;width:460px;height:31px;background:linear-gradient(90deg,var(--sage) 0%,#dde4d7 60%,rgba(255,255,255,0) 100%)}
.band-title{font-family:"Roboto Condensed",sans-serif;font-size:20px;padding:5px 0 0 61px}
.contact-details{position:absolute;left:256px;font-size:15.5px;line-height:20px}
.form-intro{position:absolute;left:256px;top:631px;font-size:15.5px;font-style:italic;font-weight:700}
.field-label{position:absolute;left:256px;width:142px;height:28px;border-radius:8px 0 0 8px;background:linear-gradient(90deg,#dce4d5,#f6f7f4);font-size:15.5px;color:var(--label-grey);padding:4px 0 0 16px}
.field-input{position:absolute;left:412px;width:329px;height:24px;border:2px solid var(--field-border);background:#fff}
.field-textarea{position:absolute;left:411px;top:883px;width:330px;height:79px;border:1px solid var(--field-border);background:#fff}
.send-button{position:absolute;left:662px;top:971px;width:73px;height:27px;border-radius:8px;background:linear-gradient(90deg,var(--lime) 0%,var(--lime-soft) 35%,var(--lime-soft) 80%,var(--lime) 100%);font-size:17px;text-align:center;padding-top:2px;box-shadow:0 1px 2px rgba(0,0,0,.3)}
.page-footer-band{position:absolute;left:196px;top:1018px;width:639px;height:58px;background:linear-gradient(90deg,var(--sage) 0%,#dfe5da 50%,#fbfbfa 100%)}
.site-footer{position:absolute;top:1088px;left:199px;display:flex;align-items:center;font-size:16.5px;color:#fff;text-shadow:0 1px 1px rgba(0,0,0,.35)}
.site-footer a{color:#fff;text-decoration:none;padding:0 9px;border-right:1px solid #fff;line-height:26px}
.site-footer a:last-of-type{border-right:none}
.copyright{position:absolute;left:704px;top:1090px;font-size:16px;color:#fff;text-shadow:0 1px 1px rgba(0,0,0,.5)}
</style>
</head>
<body>
<div class="stage">
  <div class="page">
    <div class="page-edge"></div>
    <svg class="header-swoosh" width="639" height="240" viewBox="0 0 639 240" aria-hidden="true">
      <defs>
        <linearGradient id="swooshFill" x1="0" y1="0" x2="0.4" y2="1">
          <stop offset="0" stop-color="#c9c9c9"/>
          <stop offset="0.55" stop-color="#ececec"/>
          <stop offset="1" stop-color="#ffffff"/>
        </linearGradient>
      </defs>
      <path d="M0 0 H639 V88 C450 110 200 150 0 210 Z" fill="url(#swooshFill)"/>
      <path d="M0 210 C200 150 450 110 639 88" fill="none" stroke="#bdbdbd" stroke-width="2"/>
    </svg>
    <div class="brand-mark"></div>
    <div class="brand-name">Marlow People Support</div>
    <div class="brand-tagline">Outsourced Human Resources Solutions and Stragedies</div>
  </div>

  <nav class="main-nav">
    <a href="#" style="left:700px;top:151px">Home</a>
    <a href="#" style="left:632px;top:183px">Our Services</a>
    <a href="#" class="current" style="left:601px;top:220px">Our Consultants</a>
    <a href="#" style="left:656px;top:258px">Our Fees</a>
  </nav>

  <div class="band" style="top:274px"><div class="band-title">Contact Us</div></div>
  <div class="contact-tab">Contact Us</div>

  <svg class="nav-dial" width="180" height="180" viewBox="0 0 180 180" aria-hidden="true">
    <circle cx="90" cy="90" r="84" fill="#cfcfcf" stroke="#b8b8b8" stroke-width="2"/>
    <circle cx="90" cy="90" r="66" fill="#d9d9d9"/>
    <circle cx="90" cy="90" r="60" fill="#e4e4e4"/>
    <g fill="#d6d6d6" stroke="#2aa7c9" stroke-width="2.5" stroke-linejoin="round">
      <path d="M26.3 38.4 A82 82 0 0 1 45.3 21.2 L54 34.6 A66 66 0 0 0 38.7 48.5 Z"/>
      <path d="M10.8 68.8 A82 82 0 0 1 21.2 45.3 L34.6 54 A66 66 0 0 0 26.2 72.9 Z"/>
      <path d="M9 102.8 A82 82 0 0 1 9 77.2 L24.8 79.7 A66 66 0 0 0 24.8 100.3 Z"/>
      <path d="M24.5 139.4 A82 82 0 0 1 12.4 116.7 L27.6 111.5 A66 66 0 0 0 37.3 129.7 Z"/>
    </g>
    <path d="M133.5 159.5 A82 82 0 0 1 46.5 159.5 L55 146 A66 66 0 0 0 125 146 Z" fill="#6db33f"/>
  </svg>

  <p class="contact-details" style="top:331px">Principal Consultant&nbsp; Tessa Marlow</p>
  <address class="contact-details" style="top:391px;font-style:normal">
    14b Larkin Street<br>
    Westmere&nbsp; WA&nbsp; 6099<br>
    mobile<br>
    0400 123 456<br>
    email<br>
    tessa@marlowpeoplesupport.example<br>
    web<br>
    www.marlowpeoplesupport.example
  </address>

  <div class="band" style="top:577px"></div>

  <p class="form-intro">Please fill out the form below and a Consultant will be in touch shortly.</p>

  <form class="enquiry-form">
    <label class="field-label" style="top:689px">First Name</label><div class="field-input" style="top:690px"></div>
    <label class="field-label" style="top:727px">Last Name</label><div class="field-input" style="top:728px"></div>
    <label class="field-label" style="top:765px">Company</label><div class="field-input" style="top:767px"></div>
    <label class="field-label" style="top:805px">E-mail</label><div class="field-input" style="top:806px"></div>
    <label class="field-label" style="top:844px">Phone</label><div class="field-input" style="top:846px;left:411px;width:330px"></div>
    <label class="field-label" style="top:881px">Comments</label><div class="field-textarea"></div>
    <div class="send-button">Send</div>
  </form>

  <div class="page-footer-band"></div>

  <footer>
    <nav class="site-footer">
      <a href="#" style="padding-left:10px">Home</a>
      <a href="#">Our Services</a>
      <a href="#">Our Consultants</a>
      <a href="#">Our Fees</a>
      <a href="#">Contact Us</a>
    </nav>
    <div class="copyright">Copyright 2012 ©</div>
  </footer>
</div>
</body>
</html>
```